Brantley Advisory Group provides support for renewable energy projects to utilities and suppliers

I need a professional looking business card that is both simple and elegant and unique. My clients are mostly large organizations not individuals. I am a consultant with my own company that is small but would like to give clients the impression I am larger. Smart grid, fiber optics, software, field hardware, distribution automation, substation automation, operations, energy storage/batteries, microgrids, customer service, strategy/roadmaps, conservation, Automated Metering Infrastruture (AMI or smart meters) are all areas of focus.

Target Market(s)

Utilities, suppliers, governmental agencies involved in energy. All types of energy especially natural gas and electrical. Especially renewable energy or green projects.

Contact Information for Business Card

Name - Mark Brantley Cell Phone - 425.318.2746 Email - mbrantley@brantleyag-example.com
Company - Brantley Advisory Group (logo) Title - Principal

Font styles to use
Serif
Sans Serif

Colors

Designer to choose colors to be used in the design.

Requirements
Must have
• Simple and professional and powerful.
• Unique/creative design.
Nice to have
• Utilize color scheme to accent logo colors. Maybe some geometric pattern on edge of card with color.
Should not have
• Busy, complicated, traditional

```html
<!DOCTYPE html>
<html lang="en">
<head>
<meta charset="utf-8">
<title>Brantley Advisory Group – Business Card</title>
<link href="https://fonts.googleapis.com/css2?family=Open+Sans:wght@400;700&display=swap" rel="stylesheet">
<style>
  :root {
    --backdrop: #c8c8c8;
    --card-light: #f1f1f1;
    --brand-blue: #1c3a8c;
    --brand-green: #4f8a2a;
    --text-grey: #4a4a4a;
    --card-blue: #1c3a8c;
    --facet-light: #2a68c4;
    --white: #ffffff;
  }
  * { margin: 0; padding: 0; box-sizing: border-box; }
  html, body {
    width: 1200px;
    height: 1125px;
    overflow: hidden;
    background: var(--backdrop);
    font-family: "Open Sans", Arial, sans-serif;
  }
  .canvas { position: relative; width: 1200px; height: 1125px; }
  .card {
    position: absolute;
    top: 190px;
    width: 396px;
    height: 690px;
    border-radius: 38px;
    overflow: hidden;
  }
  .card--front { left: 138px; background: var(--card-light); }
  .card--back { left: 658px; background: var(--card-blue); }

  .wordmark {
    position: absolute;
    display: flex;
    align-items: center;
    gap: 12px;
    font-weight: 700;
    line-height: 1.05;
  }
  .wordmark__square { width: 18px; height: 18px; flex: none; }
  .wordmark__name { font-size: 26px; }

  .card--front .wordmark { left: 61px; top: 78px; color: var(--brand-blue); }
  .card--front .wordmark__square { background: var(--brand-blue); }
  .card--back .wordmark { left: 85px; top: 545px; color: var(--white); }
  .card--back .wordmark__square { background: var(--white); }

  .person { position: absolute; left: 61px; top: 203px; }
  .person__name {
    font-size: 22px;
    font-weight: 700;
    color: var(--brand-blue);
    letter-spacing: 0.3px;
    line-height: 1.1;
  }
  .person__title {
    font-size: 16px;
    color: var(--brand-green);
    line-height: 1.3;
  }
  .contact { position: absolute; left: 63px; top: 274px; list-style: none; }
  .contact__item {
    display: flex;
    align-items: center;
    gap: 10px;
    font-size: 16px;
    color: var(--text-grey);
    line-height: 20px;
  }
  .contact__icon { width: 14px; height: 14px; flex: none; }

  .facet-field {
    position: absolute;
    right: 0;
    top: 0;
    width: 396px;
    height: 460px;
    background:
      radial-gradient(ellipse at 75% 30%, rgba(42,104,196,0.75) 0%, rgba(42,104,196,0.35) 40%, rgba(28,58,140,0) 72%),
      linear-gradient(200deg, rgba(24,50,120,0.5) 0%, rgba(28,58,140,0) 60%);
  }
</style>
</head>
<body>
<div class="canvas">

  <section class="card card--front" aria-label="Business card front">
    <div class="wordmark">
      <span class="wordmark__square"></span>
      <span class="wordmark__name">Brantley<br>Advisory Group</span>
    </div>

    <div class="person">
      <p class="person__name">MARK BRANTLEY</p>
      <p class="person__title">Principal</p>
    </div>

    <ul class="contact">
      <li class="contact__item">
        <svg class="contact__icon" viewBox="0 0 14 14" aria-hidden="true">
          <path d="M3 1.5 L5 1.5 L6 4.5 L4.6 5.6 C5.4 7.3 6.7 8.6 8.4 9.4 L9.5 8 L12.5 9 L12.5 11 C12.5 12 11.8 12.5 11 12.5 C5.7 12.3 1.7 8.3 1.5 3 C1.5 2.2 2 1.5 3 1.5 Z" fill="var(--brand-blue)"/>
        </svg>
        <span>425.318.2746</span>
      </li>
      <li class="contact__item">
        <svg class="contact__icon" viewBox="0 0 14 14" aria-hidden="true">
          <rect x="1" y="3" width="12" height="8.5" fill="var(--brand-blue)"/>
          <path d="M1 3 L7 8 L13 3" fill="none" stroke="var(--card-light)" stroke-width="1.2"/>
        </svg>
        <span>mbrantley@brantleyag-example.com</span>
      </li>
      <li class="contact__item">
        <svg class="contact__icon" viewBox="0 0 14 14" aria-hidden="true">
          <g fill="none" stroke="var(--brand-blue)" stroke-width="1.3">
            <circle cx="7" cy="7" r="5.8"/>
            <ellipse cx="7" cy="7" rx="2.5" ry="5.8"/>
            <line x1="1.2" y1="7" x2="12.8" y2="7"/>
            <line x1="2" y1="4.2" x2="12" y2="4.2"/>
            <line x1="2" y1="9.8" x2="12" y2="9.8"/>
          </g>
        </svg>
        <span>www.brantleyag-example.com</span>
      </li>
    </ul>
  </section>

  <section class="card card--back" aria-label="Business card back">
    <div class="facet-field" role="img" aria-label="Blue low-poly faceted network pattern with connected nodes"></div>
    <div class="wordmark">
      <span class="wordmark__square"></span>
      <span class="wordmark__name">Brantley<br>Advisory Group</span>
    </div>
  </section>

</div>
</body>
</html>
```